Italian Grape Importer needs a Wine Label Design

Uva Dorata provides home winemakers and vineyards with ultra-premium frozen wine grapes direct from Italy. Uva Dorata grapes are highly unique, as they are the only wine grapes available worldwide that are 100% Organic and have the prestigious Italian DOCG certification. We have developed a patented process for flash-freezing wine grapes, right after being picked off of our wines in Italy. This ensures unparalleled quality for the most discerning winemakers around the world.
In addition to its expanding line of premium wine grapes, Uva Dorata also imports high-quality winemaking equipment, such as wine vats, pumps, buckets, etc.
We are looking for a professional graphic designer to create a wine label for us for a wine named "Riverbo": a 50/50 blend of Cabernet Sauvignon and Merlot. In Italian, riverbo means "the encounter/meeting". This wine will be used to promote our grapes to potential customers, both home winemakers and professional wineries and vineyards.
The label should be elegant, clean and modern, yet is approachable to our target consumer (target consumer notes below).
Target Markets:
1. Intermediate and advanced home winemakers looking for high-quality wine grapes (and equipment) that is authentically Italian. These consumers typically are affluent but earthy. They often read Cellarcraft Journal – the #1 magazine for home winemaking.
2. Small vineyards that are looking to supplement their inventory with high-quality imported wine grapes.
The label should measure 4" x 6" and include the following information:
Brand Name: Uva Dorata
Uva Dorata Logo
Wine Name: Riverbo
Blend: 50/50 Cabernet Sauvignon/Merlot
Organic, DOCG, Tuscany
Look and Feel:
• Elegant
• Serious
• Modern/Traditional
• Personable but Professional
• Gender Neutral
• Upmarket
I have attached example images to demonstrate the feel that we are looking for. These are just a possible starting point. The expectation is that the label would be professional/polished.
Note:
I've added some wine labels that we've come across that have the feel that we would like for our wine label. We want it to be clean and elegant - think valdren kross, KTR, Lavelle & Boiron. One possible color to be used is Pantone 19-2524 (Dark Purple), or Pantone 19-2428 (Magenta Purple) with silver/grey/black

```html
<!DOCTYPE html>
<html lang="it">
<head>
<meta charset="utf-8">
<title>Riverbo – Uva Dorata Wine Label</title>
<link rel="stylesheet" href="https://fonts.googleapis.com/css2?family=Antonio:wght@100&family=Pinyon+Script&family=Tinos&display=swap">
<style>
  :root {
    --ink: #0b0b0b;
    --paper-top: #ffffff;
    --paper-bottom: #e6e6e6;
    --frame-light: #f3f3f3;
    --frame-dark: #dcdcdc;
  }
  * { margin: 0; padding: 0; box-sizing: border-box; }
  html, body {
    width: 1200px;
    height: 900px;
    overflow: hidden;
  }
  body {
    background: linear-gradient(to bottom, var(--paper-top) 0%, var(--paper-top) 35%, var(--paper-bottom) 100%);
    color: var(--ink);
    position: relative;
  }
  .wine-label {
    position: absolute;
    inset: 0;
  }
  .wine-name {
    position: absolute;
    top: 178px;
    left: 0;
    width: 1200px;
    text-align: center;
    font-family: "Pinyon Script", cursive;
    font-size: 86px;
    line-height: 1;
    font-weight: 400;
    color: var(--ink);
  }
  .side-bands {
    position: absolute;
    top: 319px;
    left: 263px;
    width: 674px;
    height: 293px;
  }
  .cartouche-area {
    position: absolute;
    top: 322px;
    left: 418px;
    width: 364px;
    height: 287px;
    border-radius: 40px;
    background: linear-gradient(to bottom, var(--frame-light), var(--frame-dark));
  }
  .brand-name {
    position: absolute;
    top: 400px;
    left: 0;
    width: 1200px;
    text-align: center;
    font-family: "Antonio", sans-serif;
    font-weight: 100;
    font-size: 112px;
    line-height: 1;
    letter-spacing: 0.2em;
    text-indent: 0.2em;
    color: var(--ink);
  }
  .wine-details {
    position: absolute;
    top: 636px;
    left: 0;
    width: 1200px;
    text-align: center;
    font-family: "Tinos", serif;
    font-size: 20px;
    line-height: 29px;
    letter-spacing: 0.09em;
    color: var(--ink);
  }
  .brand-dot {
    position: absolute;
    top: 712px;
    left: 593px;
    width: 14px;
    height: 14px;
    border-radius: 50%;
    background: var(--ink);
  }
</style>
</head>
<body>
  <main class="wine-label">
    <h1 class="wine-name">Riverbo</h1>

    <svg class="side-bands" viewBox="0 0 575 250" aria-hidden="true">
      <g fill="var(--ink)">
        <rect x="0" y="48" width="132" height="11"/>
        <rect x="443" y="48" width="132" height="11"/>
        <rect x="0" y="64" width="132" height="2.5"/>
        <rect x="443" y="64" width="132" height="2.5"/>
        <rect x="0" y="183.5" width="132" height="2.5"/>
        <rect x="443" y="183.5" width="132" height="2.5"/>
        <rect x="0" y="191" width="132" height="11"/>
        <rect x="443" y="191" width="132" height="11"/>
      </g>
    </svg>

    <div class="cartouche-area" role="img" aria-label="Ornamental black scrolled cartouche frame around the brand name"></div>

    <p class="brand-name" aria-label="Uva Dorata logo">UVA DORATA</p>

    <p class="wine-details">
      50/50 Cabernet Sauvignon/Merlot<br>
      Organic, DOCG, Tuscany
    </p>

    <span class="brand-dot" aria-hidden="true"></span>
  </main>
</body>
</html>
```